Skyline Signs sales for the nema region

Business card that is informative and unique. Whether the card can be applicable to a real world application or it is 3D or if something changed on the card. I want it to be an eye catcher

Went on vacation/holiday

```html
<!DOCTYPE html>
<html lang="en">
<head>
<meta charset="utf-8">
<title>Skyline Signs – Business Card</title>
<link href="https://fonts.googleapis.com/css2?family=Lato:wght@400;700&display=swap" rel="stylesheet">
<style>
  :root {
    --bg: #e9e7e4;
    --paper: #ffffff;
    --navy: #1b2f6b;
    --grey: #8f8f8f;
    --ink: #1c1c1c;
    --text: #333333;
    --sky-top: #3f74c4;
    --sky-mid: #8fb4e2;
    --sky-low: #dfe8f2;
    --rule: #bdbdbd;
  }
  * { margin: 0; padding: 0; box-sizing: border-box; }
  html, body {
    width: 1200px; height: 844px; overflow: hidden;
    background: var(--bg);
    font-family: "Lato", Arial, sans-serif;
  }
  .stage {
    position: relative; width: 1200px; height: 844px;
    display: flex; align-items: center; justify-content: center; gap: 50px;
  }
  .card {
    position: relative; width: 525px; height: 300px;
    box-shadow: 0 6px 18px rgba(0,0,0,.18);
    overflow: hidden;
  }
  /* Front */
  .card-front .sky-photo {
    position: absolute; inset: 0;
    background: linear-gradient(160deg, var(--sky-top) 0%, var(--sky-mid) 55%, var(--sky-low) 100%);
  }
  .billboard-panel {
    position: absolute; left: 225px; top: 30px; width: 270px; height: 160px;
    background: var(--paper);
    padding: 22px 16px 0 36px;
    color: var(--text);
    white-space: nowrap;
  }
  .person-name { font-size: 19px; font-weight: 700; color: var(--navy); line-height: 1; }
  .person-name .surname { color: var(--grey); }
  .person-role { font-size: 12px; margin: 3px 0 0 20px; }
  .panel-rule { height: 1px; background: var(--rule); margin: 7px 0 8px 20px; width: 140px; }
  .contact { list-style: none; font-size: 12.5px; line-height: 1.35; margin-left: 36px; }
  .contact li { white-space: nowrap; }
  .contact b { color: var(--navy); font-weight: 700; }
  .contact .web { color: var(--navy); }
  .front-brand {
    position: absolute; left: 40px; bottom: 34px;
    display: flex; align-items: center; gap: 10px;
  }
  .brand-square { width: 22px; height: 22px; background: var(--ink); }
  .front-brand .brand-name { font-size: 24px; font-weight: 400; color: var(--ink); }
  /* Back */
  .card-back { background: var(--paper); }
  .back-brand {
    position: absolute; left: 0; right: 0; top: 95px;
    display: flex; align-items: center; justify-content: center; gap: 12px;
  }
  .back-brand .brand-square { background: var(--navy); width: 26px; height: 26px; }
  .back-brand .brand-name { font-size: 34px; font-weight: 700; color: var(--navy); }
  .address {
    position: absolute; left: 0; right: 0; top: 190px;
    text-align: center; font-size: 13px; line-height: 1.5; color: var(--text);
    font-style: normal;
  }
</style>
</head>
<body>
<main class="stage">
  <section class="card card-front">
    <div class="sky-photo" role="img" aria-label="Photo of a blue sky with white clouds and a roadside billboard"></div>
    <div class="billboard-panel">
      <p class="person-name">Marcus <span class="surname">Hale</span></p>
      <p class="person-role">Managing Director</p>
      <div class="panel-rule"></div>
      <ul class="contact">
        <li><b>P:</b> 044-987 654 321</li>
        <li><b>E:</b> hello@skylinesigns.com</li>
        <li class="web">www.skylinesigns.com</li>
      </ul>
    </div>
    <div class="front-brand">
      <span class="brand-square"></span>
      <span class="brand-name">Skyline Signs</span>
    </div>
  </section>

  <section class="card card-back">
    <div class="back-brand">
      <span class="brand-square"></span>
      <span class="brand-name">Skyline Signs</span>
    </div>
    <address class="address">
      418, Harbor Road Suite 5<br>
      Zone 30210, Gulf Region
    </address>
  </section>
</main>
</body>
</html>
```